Business Card Design Project

Based on the attached logo we would like have a designed of a business card.
As we are a management, consulting company focused on business development dealing with C-level and one level below we new business cards.
We have decided to use KLR (Kestrel Growth Partners) as the business name in. The legal name will be Kestrel Growth Partners ApS but we will brand us under KLR. The tack line is “Shaping Steady Momentum” if we need one.
We want to signal the following:
- Serious
- Professional
- Creating Result
- Capable of thinking out of the box and creative
- Fast reactions we will be there when needed
What we do not want to be view as is:
- To smart
- We know better
- We can fix it yesterday
Our Value Proposition is two sited:
- Increasing revenue
- Reduced sales cost or increased efficiency
Therefore, companies can call us when they want to grow or they need to be more efficient.
Our business cards should have a two sided print with the logo incl. the tack line on one side and the detailed information on the other site.
We need to have the following information on the business cards:
- Name
- Title
- Address incl. country name (Denmark)
- Main number
- Mobile number
- E-mail address
- Wed address
Symbols are welcome to be used to guide for the above information.
Updates

Some of you has requested our specific details so here they come:

- Address incl. country name (Denmark): Lyngmosevej 42, 3470 Kildeby, Denmark

- Main number: +45 7158 3021

- Wed address: www.klrgrows.example

Mobile no. are +45 xxxx xxxx or +45 2839 4716

Our e-mail looks like this: firstname.seconname@KLRGROWS.EXAMPLE or for me: jonas.halvring@klrgrows.example

We need the design (file) as finish as posible so we just need to add personal details before printing.

Target Market(s)

C-level and one level below.

Industry/Entity Type

Legal

Font styles to use
Serif
Sans Serif

Requirements
Must have
• We would like to se suggestions with the logo (with the tackline) on one site and information on the other site where the logo should be without the tack line.
We would like to recieve recommendations for quality of paper to be used to print the business Cards on.
Nice to have
• If the information side could be used as an e-mail signature for regonition it would be viewed as a plus.

```html
<!DOCTYPE html>
<html lang="en">
<head>
<meta charset="utf-8">
<title>KLR Business Card</title>
<link href="https://fonts.googleapis.com/css2?family=Poppins:wght@400;500;700&display=swap" rel="stylesheet">
<style>
  :root {
    --bg: #2b2b2d;
    --brand-blue: #0e62b4;
    --brand-blue-light: #2a8ad8;
    --brand-blue-deep: #0a4f99;
    --card-white: #ffffff;
    --divider: #b9cde6;
    --text-blue: #1a66b8;
  }
  * { box-sizing: border-box; margin: 0; padding: 0; }
  html, body { width: 1200px; height: 900px; overflow: hidden; }
  body {
    background: var(--bg);
    font-family: "Poppins", sans-serif;
    position: relative;
  }
  .card {
    position: absolute;
    width: 580px;
    height: 332px;
    border-radius: 4px;
  }
  /* Logo side */
  .card-front {
    left: 70px;
    top: 470px;
    background: radial-gradient(ellipse at 55% 45%, var(--brand-blue-light) 0%, var(--brand-blue) 55%, var(--brand-blue-deep) 100%);
    display: flex;
    flex-direction: column;
    align-items: center;
    justify-content: center;
    color: var(--card-white);
  }
  .card-front .wordmark {
    font-weight: 700;
    font-size: 110px;
    line-height: 1;
    letter-spacing: -2px;
  }
  .card-front .tagline {
    font-weight: 500;
    font-size: 17px;
    letter-spacing: 1.5px;
    margin-top: 10px;
  }
  /* Information side */
  .card-back {
    left: 550px;
    top: 100px;
    background: var(--card-white);
    display: flex;
    align-items: center;
  }
  .card-back .logo-area {
    width: 270px;
    display: flex;
    justify-content: center;
    align-items: center;
  }
  .card-back .wordmark {
    font-weight: 700;
    font-size: 78px;
    line-height: 1;
    letter-spacing: -1px;
    color: var(--brand-blue);
  }
  .card-back .divider {
    width: 1px;
    height: 240px;
    background: var(--divider);
  }
  .details {
    padding-left: 24px;
    color: var(--text-blue);
  }
  .details .name {
    font-weight: 500;
    font-size: 22px;
    color: var(--brand-blue);
    line-height: 1.1;
  }
  .details .title {
    font-size: 15px;
    margin-bottom: 14px;
  }
  .contact-list { list-style: none; }
  .contact-list li {
    display: flex;
    align-items: center;
    font-size: 13px;
    line-height: 1.25;
    margin-bottom: 6px;
  }
  .contact-list li.address { align-items: flex-start; }
  .icon {
    width: 22px;
    height: 22px;
    flex: none;
    margin-right: 10px;
  }
</style>
</head>
<body>

<section class="card card-back" aria-label="Business card, information side">
  <div class="logo-area">
    <span class="wordmark">KLR</span>
  </div>
  <div class="divider"></div>
  <div class="details">
    <p class="name">Jonas Halvring</p>
    <p class="title">CEO/Partner</p>
    <ul class="contact-list">
      <li>
        <svg class="icon" viewBox="0 0 22 22" fill="none" stroke="currentColor" stroke-width="1.3"><circle cx="11" cy="11" r="10"/><path d="M7.5 6.5l2 .2.8 2.2-1.2 1a6 6 0 003 3l1-1.2 2.2.8.2 2c-4 1-9-4-8-8z" fill="currentColor" stroke="none"/></svg>
        +45 7158 3021
      </li>
      <li>
        <svg class="icon" viewBox="0 0 22 22" fill="none" stroke="currentColor" stroke-width="1.3"><circle cx="11" cy="11" r="10"/><rect x="8" y="5.5" width="6" height="11" rx="1"/><line x1="10" y1="14.5" x2="12" y2="14.5"/></svg>
        +45 2839 4716
      </li>
      <li>
        <svg class="icon" viewBox="0 0 22 22" fill="none" stroke="currentColor" stroke-width="1.2"><circle cx="11" cy="11" r="10"/><circle cx="11" cy="11" r="6"/><ellipse cx="11" cy="11" rx="2.6" ry="6"/><line x1="5" y1="11" x2="17" y2="11"/></svg>
        www.klrgrows.example
      </li>
      <li>
        <svg class="icon" viewBox="0 0 22 22" fill="none" stroke="currentColor" stroke-width="1.3"><circle cx="11" cy="11" r="10"/><rect x="5.5" y="7" width="11" height="8"/><path d="M5.5 7l5.5 4.5L16.5 7"/></svg>
        jonas.halvring@klrgrows.example
      </li>
      <li class="address">
        <svg class="icon" viewBox="0 0 22 22" fill="none" stroke="currentColor" stroke-width="1.3"><circle cx="11" cy="11" r="10"/><path d="M11 17s-4-4.5-4-7.5a4 4 0 018 0c0 3-4 7.5-4 7.5z" fill="currentColor" stroke="none"/><circle cx="11" cy="9.5" r="1.4" fill="#fff" stroke="none"/></svg>
        <span>Lyngmosevej 42, 3470<br>Kildeby, Denmark</span>
      </li>
    </ul>
  </div>
</section>

<section class="card card-front" aria-label="Business card, logo side">
  <span class="wordmark">KLR</span>
  <span class="tagline">Shaping Steady Momentum</span>
</section>

</body>
</html>
```